bright lane auto & van hire
rentals
this is a local car & truck rental business .. used cars ,,low rate ,, daily,, weekly mouth, and rent to own
http://www.velmorix.com/car_rental/home.do

```html
<!DOCTYPE html>
<html lang="en">
<head>
<meta charset="utf-8">
<title>Bright Lane Auto &amp; Van Hire</title>
<link rel="stylesheet" href="https://fonts.googleapis.com/css2?family=Arimo:wght@400;700&display=swap">
<style>
  :root {
    --red: #d9141b;
    --red-dark: #a80c12;
    --navy: #0f3f78;
    --sky: #bfe1f2;
    --sky-tab: #d9eef8;
    --teal: #2f8fa0;
    --teal-dark: #1d6b7c;
    --sea: #5fb3cc;
    --sea-dark: #3f93ad;
    --gold: #f6c21a;
    --page: #e4ecef;
    --white: #ffffff;
    --ink: #333333;
  }
  * { box-sizing: border-box; margin: 0; padding: 0; }
  html, body { width: 1200px; height: 869px; overflow: hidden; }
  body { font-family: "Arimo", Arial, sans-serif; color: var(--ink); background: var(--white); }
  .site { position: relative; width: 1200px; height: 869px; background: var(--white); }

  /* header */
  .brand { position: absolute; left: 120px; top: 30px; display: flex; align-items: center; gap: 14px; }
  .brand-mark { width: 54px; height: 54px; background: var(--red); }
  .brand-name { font-size: 32px; font-weight: 700; color: var(--navy); text-transform: uppercase; letter-spacing: 0.5px; line-height: 1; white-space: nowrap; }
  .contact { position: absolute; right: 26px; top: 28px; text-align: right; color: var(--navy); font-weight: 700; font-size: 17px; line-height: 22px; white-space: nowrap; }

  .main-nav { position: absolute; left: 300px; top: 86px; display: flex; gap: 5px; }
  .main-nav a { display: block; height: 34px; line-height: 34px; padding: 0 9px; background: var(--red); color: var(--white); font-size: 18px; text-decoration: none; white-space: nowrap; }

  .slogan-bar { position: absolute; left: 0; top: 120px; width: 1200px; height: 30px; background: var(--navy); }
  .slogan { position: absolute; left: 130px; top: 6px; color: var(--white); font-weight: 700; font-size: 16px; letter-spacing: 0.5px; white-space: nowrap; }
  .type-nav { position: absolute; left: 648px; top: 122px; display: flex; gap: 4px; }
  .type-nav a { display: block; height: 26px; line-height: 26px; padding: 0 14px; background: var(--sky-tab); color: var(--navy); font-size: 14px; font-weight: 700; text-decoration: none; border-radius: 4px 4px 0 0; white-space: nowrap; }
  .type-nav a.is-active { background: var(--sky); }

  /* hero */
  .hero { position: absolute; left: 0; top: 150px; width: 1200px; height: 355px; background: var(--page); }
  .booking { position: absolute; left: 96px; top: 22px; width: 480px; height: 310px; }
  .booking-tabs { display: flex; gap: 4px; height: 32px; }
  .booking-tabs span { display: block; flex: 1; height: 32px; line-height: 30px; padding: 0 10px; background: var(--teal-dark); color: var(--white); font-size: 12px; font-weight: 700; border-radius: 6px 6px 0 0; border: 2px solid #9fd3de; border-bottom: 0; white-space: nowrap; overflow: hidden; }
  .booking-tabs span.is-active { background: var(--teal); }
  .booking-form { height: 278px; background: linear-gradient(#3a9aab, var(--teal-dark)); border-radius: 0 8px 8px 8px; padding: 18px 22px; color: var(--white); font-size: 16px; }
  .field-label { margin-bottom: 6px; white-space: nowrap; }
  .bar { height: 20px; background: var(--white); border: 1px solid #9aa; }
  .row { display: flex; gap: 14px; margin-top: 4px; }
  .pair { display: flex; gap: 6px; align-items: center; width: 188px; }
  .pair .bar { width: 80px; }
  .pair .cal { width: 16px; height: 16px; background: #c33; }
  .sub-label { font-size: 14px; font-weight: 700; margin-top: 6px; display: flex; white-space: nowrap; }
  .sub-label span { width: 202px; }
  .vehicle-row { display: flex; gap: 20px; align-items: center; margin-top: 4px; }
  .select { width: 200px; height: 20px; background: var(--white); color: var(--ink); font-size: 12px; line-height: 18px; padding-left: 4px; border: 1px solid #9aa; }
  .search-btn { height: 24px; line-height: 24px; padding: 0 10px; background: var(--red); color: var(--white); font-size: 13px; border-radius: 3px; white-space: nowrap; }
  .gap { height: 18px; }

  .banner-red { position: absolute; left: 595px; top: 23px; width: 581px; height: 139px; background: linear-gradient(90deg, var(--red-dark), var(--red)); }
  .banner-red .art { position: absolute; left: 0; top: 0; width: 280px; height: 139px; background: linear-gradient(135deg, #c9c23a, #8a8a20); }
  .banner-red .line { position: absolute; right: 30px; color: var(--white); text-align: right; font-style: italic; font-weight: 700; white-space: nowrap; }
  .banner-red .line-1 { top: 38px; font-size: 20px; }
  .banner-red .line-2 { top: 62px; font-size: 38px; }
  .banner-photo { position: absolute; left: 595px; top: 167px; width: 581px; height: 168px; background: linear-gradient(90deg, #d8b8a0, #9fc2d6); }
  .banner-photo .save { position: absolute; right: 24px; bottom: 14px; color: var(--white); font-size: 38px; font-weight: 700; font-style: italic; white-space: nowrap; }

  /* offers */
  .lower { position: absolute; left: 0; top: 505px; width: 1200px; height: 364px; background: linear-gradient(var(--sea), var(--sea-dark)); }
  .offer { position: absolute; top: 18px; width: 312px; height: 173px; background: var(--white); border-radius: 4px; padding: 14px 16px; overflow: hidden; }
  .offer .car { width: 90px; height: 46px; background: linear-gradient(#e55, #a11); border-radius: 20px 20px 6px 6px; }
  .offer .price { position: absolute; left: 120px; top: 26px; width: 110px; height: 34px; line-height: 34px; background: var(--gold); color: var(--white); font-weight: 700; font-size: 26px; text-align: center; }
  .offer .ribbon { position: absolute; right: -28px; top: 20px; width: 120px; height: 22px; background: var(--red); color: var(--white); font-size: 10px; line-height: 22px; text-align: center; transform: rotate(40deg); }
  .offer h3 { color: var(--red); font-size: 14px; margin-top: 18px; white-space: nowrap; }
  .offer p { font-size: 11px; line-height: 15px; color: #444; margin-top: 4px; }

  .specialty-label { position: absolute; left: 120px; top: 215px; width: 122px; height: 92px; }
  .specialty-label span { position: absolute; left: 12px; top: 26px; color: var(--white); font-weight: 700; font-size: 17px; line-height: 21px; }
  .thumb { position: absolute; top: 203px; width: 144px; height: 144px; background: var(--white); padding: 14px; }
  .thumb div { width: 100%; height: 100%; background: linear-gradient(#ffffff, #cfd6dc); }
</style>
</head>
<body>
<div class="site">
  <header>
    <div class="brand"><span class="brand-mark"></span><span class="brand-name">Bright Lane Auto &amp; Van Hire</span></div>
    <div class="contact">ADDRESS : 418 MARROW LN DALBY NJ 08199<br>PHONE : 555-014-2290</div>
    <nav class="main-nav">
      <a href="#">rent a car</a><a href="#">rent a truck</a><a href="#">used cars</a><a href="#">low rates</a><a href="#">daily &amp; weekly rent</a><a href="#">monthly rent</a><a href="#">rent to own</a>
    </nav>
    <div class="slogan-bar"><span class="slogan">WHY BUY WHEN YOU CAN RENT TO OWN</span></div>
    <nav class="type-nav">
      <a href="#" class="is-active">Specialty Vehicles</a><a href="#">Luxury</a><a href="#">Sports Car</a><a href="#">Hybrids</a><a href="#">SUVs</a><a href="#">Vans</a>
    </nav>
  </header>

  <section class="hero">
    <div class="booking">
      <div class="booking-tabs"><span class="is-active">Search for a Rental</span><span>Your Reservations</span><span>Coupons &amp; Specials</span></div>
      <div class="booking-form">
        <div class="field-label">Choose your pickup location</div>
        <div class="bar"></div>
        <div class="gap"></div>
        <div class="field-label">Enter your dates and times</div>
        <div class="sub-label"><span>Pickup Date / Time</span><span>Return Date / Time</span></div>
        <div class="row">
          <div class="pair"><div class="bar"></div><div class="cal"></div><div class="bar"></div></div>
          <div class="pair"><div class="bar"></div><div class="cal"></div><div class="bar"></div></div>
        </div>
        <div class="gap"></div>
        <div class="field-label">Select your vehicle preference</div>
        <div class="vehicle-row"><div class="select">no preference</div><div class="search-btn">Search for Rates</div></div>
      </div>
    </div>
    <div class="banner-red">
      <div class="art" role="img" aria-label="Yellow hatchback car with a key"></div>
      <div class="line line-1">Giving you the Transport</div>
      <div class="line line-2">You need</div>
    </div>
    <div class="banner-photo" role="img" aria-label="Happy family looking out of a car window">
      <div class="save">Save 15%</div>
    </div>
  </section>

  <section class="lower">
    <article class="offer" style="left:120px">
      <div class="car" role="img" aria-label="Red compact car"></div>
      <div class="price">365$</div><div class="ribbon">Hot Deal</div>
      <h3>Lorem ipsum dolor sit amet</h3>
      <p>Clean, reliable cars for every trip. Pick up today, pay one low daily rate with free miles included.</p>
    </article>
    <article class="offer" style="left:456px">
      <div class="car" role="img" aria-label="Red compact car"></div>
      <div class="price">365$</div><div class="ribbon">Hot Deal</div>
      <h3>Lorem ipsum dolor sit amet</h3>
      <p>Clean, reliable cars for every trip. Pick up today, pay one low daily rate with free miles included.</p>
    </article>
    <article class="offer" style="left:797px">
      <div class="car" role="img" aria-label="Red compact car"></div>
      <div class="price">365$</div><div class="ribbon">Hot Deal</div>
      <h3>Lorem ipsum dolor sit amet</h3>
      <p>Clean, reliable cars for every trip. Pick up today, pay one low daily rate with free miles included.</p>
    </article>

    <div class="specialty-label">
      <svg width="122" height="92" viewBox="0 0 122 92"><path d="M0 8 L100 0 L122 46 L100 92 L0 84 Z" fill="#1f5fd6"/></svg>
      <span>Specialty<br>Vehicles</span>
    </div>
    <div class="thumb" style="left:247px"><div role="img" aria-label="Black sedan"></div></div>
    <div class="thumb" style="left:420px"><div role="img" aria-label="Black sports car"></div></div>
    <div class="thumb" style="left:588px"><div role="img" aria-label="Blue small city car"></div></div>
    <div class="thumb" style="left:758px"><div role="img" aria-label="Grey SUV"></div></div>
    <div class="thumb" style="left:929px"><div role="img" aria-label="Silver van"></div></div>
  </section>
</div>
</body>
</html>
```